Cover Art for Song "Driftin Past Noon" by Dale Pommery

Link to song
https://www.tunelatchhub.com/dalepommerythehometownheroes

Lyrics:
Driftin’ Past Noon

Verse:
I lost my way
and I can’t be found
Gettin too old,
a little run-down
Always in trouble Gonna pick things up
Trouble finds me
Wherever I am
Need a new direction
Need a new plan
Gonna make a change
Pre Chorus
some don’t see it and
others don’t know
listen on up
I’m moving on down
I'm movin down
Chorus
Im Driftin Past Noon to the Everglades
where nobody seems to make
a big deal who I am

Target Market(s)

Country Music

Industry/Entity Type

Music

```html
<!DOCTYPE html>
<html lang="en">
<head>
<meta charset="utf-8">
<title>Driftin’ Past Noon – Dale Pommery</title>
<link rel="stylesheet" href="https://fonts.googleapis.com/css2?family=Cinzel:wght@400;700&display=swap">
<style>
  :root {
    --sky-top: #8a4a32;
    --sky-ember: #e0622a;
    --sky-teal: #7fb8a8;
    --sun-glow: #ffe680;
    --horizon: #f3b53a;
    --marsh-green: #6f7a32;
    --marsh-deep: #2f3a22;
    --boardwalk: #9a5e2f;
    --boardwalk-dark: #4d2c18;
    --title-ink: rgba(58, 30, 18, 0.55);
    --name-yellow: #f2e21a;
  }
  html, body {
    margin: 0;
    padding: 0;
    width: 1200px;
    height: 1200px;
    overflow: hidden;
    background: #ffffff;
  }
  .cover {
    position: relative;
    width: 1200px;
    height: 1200px;
    overflow: hidden;
  }
  .cover-scene {
    position: absolute;
    inset: 0;
    background:
      radial-gradient(ellipse 22% 30% at 50% 84%, var(--boardwalk) 0%, rgba(154, 94, 47, 0.85) 45%, rgba(77, 44, 24, 0) 100%),
      radial-gradient(ellipse 38% 22% at 58% 36%, var(--sun-glow) 0%, rgba(243, 181, 58, 0.7) 45%, rgba(243, 181, 58, 0) 100%),
      radial-gradient(ellipse 35% 25% at 88% 14%, var(--sky-teal) 0%, rgba(127, 184, 168, 0) 100%),
      linear-gradient(180deg,
        var(--sky-top) 0%,
        var(--sky-ember) 18%,
        #f08a34 32%,
        var(--horizon) 42%,
        #c9a542 46%,
        var(--marsh-green) 56%,
        #4f5a2c 72%,
        var(--marsh-deep) 100%);
  }
  .cover-title {
    position: absolute;
    left: 0;
    right: 0;
    top: 300px;
    margin: 0;
    text-align: center;
    font-family: "Cinzel", "Times New Roman", serif;
    font-weight: 700;
    font-size: 168px;
    line-height: 0.86;
    letter-spacing: 2px;
    color: var(--title-ink);
    text-transform: uppercase;
  }
  .cover-title .line { display: block; }
  .cover-title .line-noon { margin-top: 40px; }
  .cover-artist {
    position: absolute;
    left: 0;
    right: 0;
    top: 890px;
    margin: 0;
    text-align: center;
    font-family: "Cinzel", "Times New Roman", serif;
    font-weight: 400;
    font-size: 42px;
    letter-spacing: 12px;
    color: var(--name-yellow);
    text-transform: uppercase;
  }
</style>
</head>
<body>
  <main class="cover">
    <div class="cover-scene" role="img" aria-label="Painted scene: a man seen from behind walks along a wooden boardwalk through marsh grass toward a blazing orange and yellow sunset sky"></div>
    <h1 class="cover-title">
      <span class="line line-driftin">Driftin</span>
      <span class="line line-past">Past</span>
      <span class="line line-noon">Noon</span>
    </h1>
    <p class="cover-artist">Dale Pommery</p>
  </main>
</body>
</html>
```